K7 Morvane Advisory Partners Ltd - Website Design

We already have a company logo. We need a website created for our consulting agency.
Refer to attached files for logo and website content.
We would also be open to any additional recommendations.
Industry/Entity Type
Finance And Accounting
Coding
Coded - Design and coding required
Number of Pages Required
1 page
Font styles to use
Serif
Colors
3377b5
b868aa
33b8a4
Requirements
Must have
- Company Logo, name and who we are.

```html
<!DOCTYPE html>
<html lang="en">
<head>
<meta charset="utf-8">
<title>K7 Morvane Advisory Partners Ltd</title>
<link rel="stylesheet" href="https://fonts.googleapis.com/css2?family=Play:wght@400;700&family=Open+Sans:wght@400;600;700&display=swap">
<style>
  :root {
    --blue: #2f67b0;
    --blue-bright: #3377b5;
    --navy: #1d0f5e;
    --hero-blue: #2b62ad;
    --teal: #33b8a4;
    --purple: #a94f9a;
    --ink: #222;
    --muted: #555;
    --white: #fff;
    --footer: #0c0c0c;
  }
  * { margin: 0; padding: 0; box-sizing: border-box; }
  html, body { width: 1200px; height: 4100px; overflow: hidden; background: var(--white); }
  body { position: relative; font-family: "Open Sans", Arial, sans-serif; color: var(--ink); }
  .abs { position: absolute; }

  /* header */
  .site-header { position: absolute; left: 0; top: 0; width: 1200px; height: 122px; background: var(--white); box-shadow: 0 2px 6px rgba(0,0,0,.08); z-index: 2; }
  .brand { position: absolute; left: 108px; top: 34px; display: flex; align-items: center; gap: 10px; font-family: "Play", sans-serif; font-size: 24px; color: var(--navy); }
  .brand-mark { width: 14px; height: 14px; border-radius: 50%; background: var(--navy); }
  .nav { position: absolute; top: 50px; font-size: 14px; color: var(--ink); }

  /* hero */
  .hero { position: absolute; left: 0; top: 122px; width: 1200px; height: 538px; overflow: hidden; }
  .hero-bg { position: absolute; inset: 0; }
  .hero-bar { position: absolute; left: 372px; top: 115px; width: 55px; height: 10px; background: var(--teal); }
  .hero-welcome { position: absolute; left: 0; width: 802px; top: 145px; text-align: center; font-family: "Play", sans-serif; font-weight: 700; font-size: 28px; color: var(--white); }
  .hero-title { position: absolute; left: 0; width: 802px; top: 190px; text-align: center; font-family: "Play", sans-serif; font-size: 80px; line-height: 1; letter-spacing: 2px; color: var(--white); }
  .hero-sub { position: absolute; left: 0; width: 822px; top: 293px; text-align: center; font-family: "Open Sans", sans-serif; font-size: 27px; color: var(--white); letter-spacing: 1px; }
  .hero-art { position: absolute; left: 668px; top: 68px; width: 532px; height: 470px; border-radius: 240px 0 0 200px; background: linear-gradient(160deg, #e4effb 0%, #b9d2ef 60%, #5b86c8 100%); }

  /* section headings */
  .section-bar { position: absolute; left: 571px; width: 56px; height: 9px; background: var(--teal); }
  .section-title { position: absolute; left: 0; width: 1200px; text-align: center; font-family: "Play", sans-serif; font-weight: 700; font-size: 47px; color: var(--blue); }
  .intro { position: absolute; left: 0; width: 1200px; top: 836px; text-align: center; font-size: 20px; line-height: 32px; color: var(--ink); }

  /* services */
  .service-title { position: absolute; font-family: "Play", sans-serif; font-weight: 700; font-size: 37px; color: var(--blue); white-space: nowrap; }
  .service-list { position: absolute; list-style: none; font-size: 16px; line-height: 31px; color: var(--ink); }
  .service-list li { position: relative; padding-left: 36px; white-space: nowrap; }
  .service-list li::before { content: ""; position: absolute; left: 2px; top: 11px; width: 8px; height: 8px; border-top: 1.5px solid #666; border-right: 1.5px solid #666; transform: rotate(45deg); }
  .art { position: absolute; border-radius: 10px; background: linear-gradient(150deg, #f3f6fb 0%, #e4edf8 55%, #dff3ef 100%); }

  /* contact */
  .contact-band { position: absolute; left: 0; top: 3536px; width: 1200px; height: 451px; }
  .quick { position: absolute; left: 0; top: 0; width: 654px; height: 451px; background: var(--purple); }
  .quick-title { position: absolute; left: 115px; top: 68px; font-family: "Play", sans-serif; font-weight: 700; font-size: 25px; color: var(--white); }
  .field { position: absolute; left: 108px; width: 473px; background: var(--white); font-size: 12px; color: var(--ink); padding: 0 20px; }
  .field span { position: absolute; left: 20px; }
  .submit { position: absolute; left: 277px; top: 379px; width: 137px; height: 40px; border-radius: 20px; background: var(--blue); color: var(--white); font-weight: 700; font-size: 15px; text-align: center; line-height: 40px; }
  .contact-bar { position: absolute; left: 756px; top: 50px; width: 56px; height: 9px; background: var(--teal); }
  .contact-title { position: absolute; left: 756px; top: 80px; font-family: "Play", sans-serif; font-weight: 700; font-size: 47px; color: var(--blue); }
  .contact-line { position: absolute; left: 756px; display: flex; align-items: center; gap: 22px; color: var(--ink); }
  .contact-line svg { width: 26px; height: 26px; }
  .contact-email { top: 170px; font-size: 21px; }
  .contact-phone { top: 225px; font-size: 30px; font-weight: 700; }

  /* footer */
  .site-footer { position: absolute; left: 0; top: 3987px; width: 1200px; height: 113px; background: var(--footer); }
  .copyright { position: absolute; left: 0; width: 1200px; top: 49px; text-align: center; font-size: 13px; color: var(--white); }
  .to-top { position: absolute; left: 1066px; top: 38px; width: 16px; height: 12px; }
</style>
</head>
<body>

<header class="site-header">
  <div class="brand"><span class="brand-mark"></span>K7 Morvane</div>
  <a class="nav" style="left:789px">Who we are?</a>
  <a class="nav" style="left:920px">Services</a>
  <a class="nav" style="left:1019px">Contact Us</a>
</header>

<section class="hero">
  <svg class="hero-bg" viewBox="0 0 1200 538" preserveAspectRatio="none">
    <rect width="1200" height="538" fill="#2b62ad"/>
    <path d="M0 0 H900 C860 90 700 120 560 200 C420 290 440 420 300 538 H0 Z" fill="#2f58a3"/>
    <path d="M0 0 H860 C830 70 680 110 540 180 C400 260 410 400 260 538 H0 Z" fill="#1d0f5e"/>
  </svg>
  <div class="hero-art" role="img" aria-label="Illustration of two colleagues working at a desk with a laptop, calculator and charts"></div>
  <div class="hero-bar"></div>
  <div class="hero-welcome">Welcome To</div>
  <h1 class="hero-title">K7 MORVANE</h1>
  <div class="hero-sub">ADVISORY PARTNERS LTD.</div>
</section>

<div class="section-bar" style="top:740px"></div>
<h2 class="section-title" style="top:764px">Who we are?</h2>
<p class="intro">We are a boutique Financial Management Agency that provides specialized<br>services for small and medium sized enterprises</p>

<div class="section-bar" style="top:979px"></div>
<h2 class="section-title" style="top:996px">Services offered?</h2>

<!-- Accounting -->
<h3 class="service-title" style="left:108px;top:1140px">Accounting</h3>
<ul class="service-list" style="left:108px;top:1203px">
  <li>Preparation of financial reports</li>
  <li>Regulatory compliance</li>
  <li>Compensation planning</li>
  <li>Corporate tax consulting</li>
  <li>Accounting system implementation and migrations</li>
</ul>
<div class="art" style="left:641px;top:1087px;width:362px;height:361px" role="img" aria-label="Illustration of a person carrying a money bag beside a phone and coins"></div>

<!-- Bookkeeping -->
<div class="art" style="left:143px;top:1385px;width:330px;height:310px" role="img" aria-label="Illustration of a light bulb with a brain, books and a person holding a pencil"></div>
<h3 class="service-title" style="left:616px;top:1448px">Bookkeeping</h3>
<ul class="service-list" style="left:611px;top:1510px">
  <li>Contrary to popular belief</li>
  <li>Duis aute irure dolor in reprehenderit</li>
  <li>Nor again is there anyone who loves or pursues</li>
  <li>Quis autem vel eum iure reprehenderit</li>
</ul>

<!-- Financial Management -->
<h3 class="service-title" style="left:116px;top:1717px">Financial Management</h3>
<ul class="service-list" style="left:116px;top:1780px">
  <li>Cash flow management</li>
  <li>Financial and management reporting</li>
  <li>Budgeting and forecasting</li>
  <li>Technical accounting advisory</li>
  <li>Business plan preparation</li>
  <li>Finance process improvements</li>
  <li>Governance</li>
  <li>Secure financing</li>
  <li>Lease accounting</li>
  <li>Expense management</li>
</ul>
<div class="art" style="left:617px;top:1751px;width:370px;height:366px" role="img" aria-label="Illustration of a person beside a laptop showing a rising bar chart"></div>

<!-- Government Grants -->
<div class="art" style="left:119px;top:2141px;width:343px;height:310px" role="img" aria-label="Illustration of a person with a phone showing a government building and a bank card"></div>
<h3 class="service-title" style="left:617px;top:2210px">Government Grants</h3>
<ul class="service-list" style="left:617px;top:2274px">
  <li>Process applications for government grants<br>and tax breaks</li>
</ul>

<!-- Strategy -->
<h3 class="service-title" style="left:110px;top:2471px">Strategy</h3>
<ul class="service-list" style="left:110px;top:2533px">
  <li>Operational governance</li>
  <li>Market research</li>
  <li>Sales &amp; marketing analysis</li>
  <li>Growth strategies</li>
  <li>Decision management</li>
  <li>Operations optimization</li>
  <li>Third party vendor assessments</li>
  <li>Systems transformations</li>
</ul>
<div class="art" style="left:637px;top:2459px;width:394px;height:358px" role="img" aria-label="Illustration of a person presenting a laptop dashboard with pie and bar charts"></div>

<!-- Mergers and Acquisitions -->
<div class="art" style="left:143px;top:2841px;width:331px;height:318px" role="img" aria-label="Illustration of a person signing a large contract with a pen"></div>
<h3 class="service-title" style="left:610px;top:2858px">Mergers and Acquisitions</h3>
<ul class="service-list" style="left:609px;top:2921px">
  <li>Operations due diligence</li>
  <li>Integration services</li>
</ul>

<!-- Internal Audit -->
<h3 class="service-title" style="left:110px;top:3151px">Internal Audit</h3>
<ul class="service-list" style="left:110px;top:3214px">
  <li>Audit and review of financial and non-financial information</li>
  <li>Internal control reviews</li>
  <li>Assessment of Business Risk</li>
  <li>Review of suppliers</li>
  <li>Viability reviews</li>
</ul>
<div class="art" style="left:645px;top:3111px;width:374px;height:358px" role="img" aria-label="Illustration of a person with a pencil beside a balance sheet clipboard and calculator"></div>

<!-- Contact -->
<section class="contact-band">
  <div class="quick">
    <div class="quick-title">Quick Contact</div>
    <div class="field" style="top:118px;height:43px"><span style="top:14px">Name</span></div>
    <div class="field" style="top:177px;height:41px"><span style="top:13px">Email</span></div>
    <div class="field" style="top:234px;height:115px"><span style="top:16px">Message</span></div>
    <div class="submit">Submit</div>
  </div>
  <div class="contact-bar"></div>
  <h2 class="contact-title">Contact Us</h2>
  <div class="contact-line contact-email">
    <svg viewBox="0 0 24 24" fill="none" stroke="#2f67b0" stroke-width="2"><rect x="2" y="5" width="20" height="14" rx="1"/><path d="M2 6l10 7 10-7"/></svg>
    info@morvaneadvisory.com
  </div>
  <div class="contact-line contact-phone">
    <svg viewBox="0 0 24 24" fill="#2f67b0"><path d="M6.6 10.8a15.1 15.1 0 006.6 6.6l2.2-2.2c.3-.3.7-.4 1-.2 1.1.4 2.3.6 3.6.6.6 0 1 .4 1 1V20c0 .6-.4 1-1 1A17 17 0 013 4c0-.6.4-1 1-1h3.5c.6 0 1 .4 1 1 0 1.3.2 2.5.6 3.6.1.3 0 .7-.2 1z"/></svg>
    1-800 555 0142
  </div>
</section>

<footer class="site-footer">
  <div class="copyright">© 2021 &nbsp;|&nbsp; www.morvaneadvisory.com</div>
  <svg class="to-top" viewBox="0 0 16 12" fill="none" stroke="#fff" stroke-width="2"><path d="M2 10l6-6 6 6"/></svg>
</footer>

</body>
</html>
```